Redesign PixelHarbor's Designer Account Home Page

Are a web designer? New to PixelHarbor? This contest is for you!

We want you to redesign PixelHarbor's designer account home page. We're looking for bold and innovative ideas to make this page a useful and fun experience for you and your fellow designers.

Only new registrants this month are eligible to enter this contest and win prizes.

Your task:
* We want you to put your web design skills to the test and re-design the My Account home page ("Overview") on PixelHarbor to make it more functional and engaging for designers on PixelHarbor.
* The page you are redesigning is here: http://www.pixelharbor-example.com/my-profile.
* Your design should allow for the same functionality as the existing page, though you don't need to replicate the same elements (buttons) or the same menu structure.
* Your design must fit with the branding of the site.
* You must provide a brief outline of what changes you made and why when you upload your design
* 1 submission per designer - make it your best work!
* Pls see "Must haves" for requirements.

Deadline:
* Submit before 12:00am 1st September UTC. Pls convert this deadline to your local timezone and take note of the local time and date

Prizes: $1,000 to win
* First prize for the best design is $700
* Second prize is $200
* Third prize is $100

If you started from scratch, how would you design the MyAccount page on PixelHarbor?

Good luck & have fun!

Mel / The PixelHarbor Team

Target Market(s)

PixelHarbor designers

Number of Pages Required

1 page

Requirements
Must have
• Dimensions: 1200 x 1000 px
• Minimum 150-300 dpi
• Your design must adhere to our quality standards to be eligible to receive a prize
• Submissions must be created in Adobe Creative Suite (Illustrator or Photoshop)
• Your design must fit with the branding of the PixelHarbor site.
• Only new registrants this month are eligible to enter and win prizes.

```html
<!DOCTYPE html>
<html lang="en">
<head>
<meta charset="utf-8">
<title>PixelHarbor – My Profile Overview</title>
<link rel="stylesheet" href="https://fonts.googleapis.com/css2?family=Open+Sans:wght@400;600;700&display=swap">
<style>
  :root{
    --page:#eeeeee;
    --card:#ffffff;
    --line:#dcdcdc;
    --text:#444444;
    --ink:#333333;
    --muted:#8c8c8c;
    --blue:#2b8bcf;
    --blue-dark:#1f6fa8;
    --green:#7dbb2f;
    --green-dark:#5f9820;
    --row:#eef1f4;
    --footer:#2a2a2a;
    --footer-bottom:#1c1c1c;
    --footer-text:#a9a9a9;
    --red:#d9463b;
  }
  *{box-sizing:border-box;margin:0;padding:0}
  html,body{width:805px;height:1200px;overflow:hidden}
  body{position:relative;background:var(--page);font-family:"Open Sans",Arial,sans-serif;color:var(--text);font-size:9px}

  /* top bar */
  .site-header{position:absolute;left:0;top:0;width:805px;height:42px;background:linear-gradient(#ffffff,#f1f1f1);border-bottom:1px solid var(--line)}
  .brand{position:absolute;left:24px;top:12px;font-size:15px;font-weight:700;color:var(--ink);line-height:18px}
  .main-nav{position:absolute;left:160px;top:15px;display:flex;gap:12px;font-size:9px;color:#555}
  .nav-flag{width:14px;height:9px;background:#2c4a8f;margin-top:1px}
  .account-nav{position:absolute;right:22px;top:11px;display:flex;gap:6px}
  .account-menu{height:20px;padding:0 18px 0 8px;border:1px solid var(--line);background:#fff;line-height:18px;font-size:9px;position:relative}
  .account-menu::after{content:"";position:absolute;right:6px;top:8px;border:3px solid transparent;border-top-color:#777}
  .cta{height:20px;padding:0 10px;background:var(--green);color:#fff;line-height:20px;font-weight:600;border-radius:2px}

  .breadcrumb{position:absolute;left:0;top:42px;width:805px;height:20px;background:#e2e2e2;border-bottom:1px solid #d2d2d2;display:flex;align-items:center;padding-left:24px;gap:8px;font-size:8px;color:#666}
  .crumb-home{display:flex;align-items:center;gap:4px}

  .page-title{position:absolute;left:0;top:74px;width:805px;text-align:center;font-size:20px;font-weight:700;color:var(--ink)}
  .title-rule{position:absolute;left:70px;top:112px;width:668px;height:1px;background:var(--line)}

  /* sidebar */
  .sidebar{position:absolute;left:70px;top:136px;width:152px}
  .browse-btn{display:block;height:30px;background:var(--green);border-bottom:3px solid var(--green-dark);color:#fff;font-size:13px;font-weight:700;line-height:28px;padding-left:12px}
  .side-menu{list-style:none;margin-top:12px;background:#fff;border:1px solid var(--line)}
  .side-menu li{height:19px;line-height:19px;padding-left:22px;border-bottom:1px solid #ececec;color:#777;font-size:8px;position:relative}
  .side-menu li::before{content:"";position:absolute;left:8px;top:7px;width:6px;height:5px;background:#bbb}
  .side-menu li::after{content:"›";position:absolute;right:8px;color:#aaa}
  .side-menu li.active{background:var(--blue);color:#fff}
  .side-menu li.active::before{background:#fff}
  .side-menu li.active::after{color:#fff}

  /* cards */
  .card{position:absolute;background:var(--card);border:1px solid var(--line)}
  .profile-card{left:241px;top:132px;width:497px;height:112px}
  .avatar{position:absolute;left:22px;top:32px;width:40px;height:40px;background:#dde6ee;border:1px solid #cfd8e0}
  .stats{position:absolute;left:86px;top:24px;display:flex}
  .stat{width:100px;text-align:center;border-left:1px solid #eee}
  .stat:first-child{border-left:0}
  .stat-label{font-size:8px;color:var(--muted)}
  .stat-value{font-size:17px;color:#666;margin:3px 0}
  .stat-note{font-size:6.5px;color:#aaa}

  .progress-card{left:241px;top:254px;width:497px;height:354px;text-align:center}
  .progress-title{margin-top:16px;font-size:16px;font-weight:600;color:var(--text)}
  .progress-value{margin-top:6px;font-size:44px;font-weight:400;color:var(--blue);line-height:1.1}
  .progress-bar{width:330px;height:14px;margin:10px auto 0;background:#dfe7ee}
  .progress-fill{width:57%;height:100%;background:var(--blue)}
  .section-rule{height:1px;background:var(--line);margin:22px 0 0}
  .todo-title{margin-top:10px;font-size:18px;font-weight:700;color:var(--text)}
  .todo-list{list-style:none;width:420px;margin:12px auto 0;text-align:left}
  .todo-list li{height:20px;line-height:20px;padding-left:8px;font-size:8px;color:#999;position:relative}
  .todo-list li:nth-child(odd){background:var(--row)}
  .todo-list li.open{color:#555}
  .complete-btn{position:absolute;right:0;top:2px;height:16px;line-height:16px;padding:0 8px;background:var(--blue);color:#fff;font-size:7.5px}

  .panel{top:668px;width:237px;height:272px}
  .jobs-panel{left:241px}
  .achieve-panel{left:501px}
  .panel-head{height:24px;background:var(--blue);color:#fff;text-align:center;font-size:11px;font-weight:700;line-height:24px}
  .panel-body{padding:8px 10px;font-size:7px;color:#777;line-height:1.45}
  .job{border-top:1px solid #eee;padding:7px 0 6px;margin-top:6px}
  .job-title{color:var(--blue);font-weight:600;font-size:7.5px;white-space:nowrap;overflow:hidden;text-overflow:ellipsis}
  .job-meta{display:flex;gap:14px;margin-top:4px;color:#888}
  .meta-item{display:flex;align-items:center;gap:4px}
  .meta-icon{width:7px;height:6px;background:#bbb}
  .pager{display:flex;justify-content:space-between;margin-top:40px;color:#888}
  .achievement{display:flex;gap:8px;align-items:center;background:var(--row);padding:5px;margin-top:7px}
  .badge{width:24px;height:24px;border-radius:50%;background:var(--blue);flex:none}
  .badge.alt{background:#9ec9e8}
  .ach-name{color:var(--blue);font-weight:600}

  /* footer */
  .site-footer{position:absolute;left:0;top:985px;width:805px;height:190px;background:var(--footer);color:var(--footer-text);font-size:7px}
  .footer-col{position:absolute;top:16px}
  .footer-col h4{font-size:10px;color:#fff;font-weight:700;margin-bottom:8px}
  .footer-col ul{list-style:none;line-height:1.9}
  .tags{display:flex;flex-wrap:wrap;gap:4px;width:170px}
  .tags span{border:1px solid #555;padding:1px 4px}
  .subscribe{left:528px;width:250px}
  .subscribe-row{display:flex}
  .subscribe-row .field{width:130px;height:16px;background:#fff;color:#999;padding-left:5px;line-height:16px}
  .subscribe-row .go{height:16px;padding:0 8px;background:var(--green);color:#fff;line-height:16px}
  .socials{display:flex;gap:6px;margin-top:14px}
  .socials span{width:20px;height:20px;border-radius:50%}
  .flags{display:flex;gap:5px;margin-top:16px}
  .flags span{width:16px;height:11px}
  .footer-brand{margin-top:12px;font-size:13px;font-weight:700;color:#fff;line-height:16px}
  .footer-bottom{position:absolute;left:0;top:1175px;width:805px;height:25px;background:var(--footer-bottom);color:#777;font-size:7px;text-align:center;line-height:25px}
</style>
</head>
<body>

<header class="site-header">
  <div class="brand">PixelHarbor</div>
  <nav class="main-nav">
    <span>Categories</span><span>Designers</span><span>Browse Jobs</span><span>How it works</span><span class="nav-flag"></span>
  </nav>
  <div class="account-nav">
    <div class="account-menu">My Profile</div>
    <div class="cta">Start a project</div>
  </div>
</header>

<div class="breadcrumb">
  <span class="crumb-home">
    <svg width="9" height="8" viewBox="0 0 9 8"><path d="M4.5 0 9 4H7.5v4h-2V5.5h-2V8h-2V4H0z" fill="#777"/></svg>Home
  </span>
  <span>›</span><span>My Profile</span>
</div>

<h1 class="page-title">Overview</h1>
<div class="title-rule"></div>

<aside class="sidebar">
  <a class="browse-btn">Browse Jobs</a>
  <ul class="side-menu">
    <li class="active">Overview</li>
    <li>Portfolio</li>
    <li>Contests</li>
    <li>Quotations</li>
    <li>Messages</li>
    <li>Invitations</li>
    <li>Payments</li>
    <li>Settings</li>
  </ul>
</aside>

<section class="card profile-card">
  <div class="avatar" role="img" aria-label="Designer profile picture placeholder"></div>
  <div class="stats">
    <div class="stat"><div class="stat-label">Rank</div><div class="stat-value">#435699</div><div class="stat-note">of 512,330 designers</div></div>
    <div class="stat"><div class="stat-label">Positive</div><div class="stat-value">0%</div><div class="stat-note">no ratings yet</div></div>
    <div class="stat"><div class="stat-label">Submissions</div><div class="stat-value">0</div><div class="stat-note">since December</div></div>
    <div class="stat"><div class="stat-label">Earnings</div><div class="stat-value">$0.00</div><div class="stat-note">withdrawable $0.00</div></div>
  </div>
</section>

<section class="card progress-card">
  <h2 class="progress-title">Getting Started Complete Your Profile</h2>
  <div class="progress-value">57 %</div>
  <div class="progress-bar"><div class="progress-fill"></div></div>
  <div class="section-rule"></div>
  <h2 class="todo-title">Things left to do:</h2>
  <ul class="todo-list">
    <li>Tell us what types of designs you do</li>
    <li class="open">Verify your payment address<span class="complete-btn">Complete</span></li>
    <li>Visit the job board</li>
    <li class="open">Add your profile pic<span class="complete-btn">Complete</span></li>
    <li>Add an about me to your profile</li>
    <li>Review and accept the designer quality standards</li>
    <li>Submit your first design</li>
  </ul>
</section>

<section class="card panel jobs-panel">
  <div class="panel-head">Recommended Jobs</div>
  <div class="panel-body">
    <p>There is over $3000 in waiting for you on these jobs that don't have any submissions yet.</p>
    <div class="job">
      <div class="job-title">Modern, funky architectural property development...</div>
      <div class="job-meta"><span class="meta-item"><i class="meta-icon"></i>14 days left</span><span class="meta-item"><i class="meta-icon"></i>$300 USD</span></div>
    </div>
    <div class="job">
      <div class="job-title">Modern, funky architectural property development...</div>
      <div class="job-meta"><span class="meta-item"><i class="meta-icon"></i>14 days left</span><span class="meta-item"><i class="meta-icon"></i>$300 USD</span></div>
    </div>
    <div class="pager"><span>Page 1</span><span>« Prev Next »</span></div>
  </div>
</section>

<section class="card panel achieve-panel">
  <div class="panel-head">Achievements</div>
  <div class="panel-body">
    <p>Earn designer-level achievements as you compete on the site.</p>
    <div class="achievement"><span class="badge"></span><div><div class="ach-name">Rookie (New)</div>Submit at least 1 design to contests</div></div>
    <div class="achievement"><span class="badge alt"></span><div><div class="ach-name">The start of something beautiful (New)</div>Submit at least 1 design to contests</div></div>
    <div class="achievement"><span class="badge"></span><div><div class="ach-name">Top 1000 Designer (New)</div>Submit at least 1 design to contests</div></div>
  </div>
</section>

<footer class="site-footer">
  <div class="footer-col" style="left:24px">
    <h4>I need a...</h4>
    <ul><li>Logo Design</li><li>Web Design</li><li>Business Card</li><li>Brochure Design</li><li>Packaging</li><li>T-Shirt Design</li><li>Illustration</li></ul>
  </div>
  <div class="footer-col" style="left:130px">
    <h4>Find a...</h4>
    <ul><li>Logo Designer</li><li>Web Designer</li><li>Graphic Designer</li><li>Freelancer</li><li>Illustrator</li><li>Print Designer</li></ul>
  </div>
  <div class="footer-col" style="left:228px">
    <h4>About us</h4>
    <ul><li>Our story</li><li>Team</li><li>Press</li><li>Careers</li><li>Contact us</li><li>Blog</li><li>Terms</li></ul>
  </div>
  <div class="footer-col" style="left:326px">
    <h4>Popular pages</h4>
    <div class="tags"><span>Logo ideas</span><span>Web layouts</span><span>Flyers</span><span>Posters</span><span>Icons</span><span>Labels</span><span>Banners</span><span>Menus</span><span>Invites</span><span>Letterhead</span><span>Signage</span><span>Stationery</span></div>
  </div>
  <div class="footer-col subscribe">
    <h4>Subscribe to our newsletter</h4>
    <div class="subscribe-row"><span class="field">Your email</span><span class="go">Subscribe</span></div>
    <div class="socials">
      <span style="background:#3b9ad9"></span><span style="background:var(--red)"></span><span style="background:#3b5fa0"></span><span style="background:var(--red)"></span>
    </div>
    <div class="flags">
      <span style="background:#c8102e"></span><span style="background:#1f3f8f"></span><span style="background:#e8e8e8"></span><span style="background:#1f3f8f"></span><span style="background:#f29a2e"></span>
    </div>
    <div class="footer-brand">PixelHarbor</div>
  </div>
</footer>
<div class="footer-bottom">Copyright © 2013 PixelHarbor Pty Ltd. All rights reserved. Terms of use | Privacy policy</div>

</body>
</html>
```